Nourish Kin Network Australia needs a flyer to update to new style guide and modernise

Nourish Kin Network Australia (NKNA) is looking to update their flyers. NKNA is a volunteer, parent-led, not for profit organisation that supports and advocates for parents and carers of someone with an eating disorder. Attached is some flyers and brochures that we are currently working with, since producing those we have introduced a style guide, also attached. The flyer needs to be visually appealing and professional.We are hoping to combine the NKNA flyer and NKNA Brochure into a single item. We also need to add in our new Uplift support groups.This would replace the back page of the brochure ("NKNA Will endeavour to facilitate and advocate...) Please refer to last pages of style guide for Uplift details.If the document could be produced to allow changes to wording as certain details will need to be refined or edited in the future.

Target Market(s)

Parents and Carers of someone with a life threatening mental illness

Font styles to use
Other font styles liked:
• Avenir Next

Colors

Designer to choose colors to be used in the design.

Requirements
Must have
• NKNA logos and font matching style guide
Nice to have
• Clean and professional looking design, visually appealing
• Easy to read
Should not have
• Upsetting images

```html
<!DOCTYPE html>
<html lang="en">
<head>
<meta charset="utf-8">
<title>NKNA Flyer</title>
<link href="https://fonts.googleapis.com/css2?family=Fjalla+One&family=Montserrat:wght@500;600;700&family=Lato:wght@400;700&display=swap" rel="stylesheet">
<style>
:root{
  --bg:#e4e4e4;
  --paper:#ffffff;
  --blue:#5ec4dd;
  --blue-deep:#2b5fa6;
  --purple:#87297f;
  --green:#4fa82a;
  --green-dark:#1f7a2a;
  --ink:#2b2b2b;
}
*{box-sizing:border-box;margin:0;padding:0}
html,body{width:1200px;height:2291px;overflow:hidden;background:var(--bg)}
body{position:relative;font-family:"Lato",sans-serif;color:var(--ink)}
.page{position:absolute;left:210px;width:780px;height:1080px;background:var(--paper);overflow:hidden;box-shadow:0 6px 24px rgba(0,0,0,.18)}
.page--front{top:50px}
.page--back{top:1161px}
.abs{position:absolute}

.brand{display:flex;align-items:center;gap:8px;white-space:nowrap}
.brand__dot{width:34px;height:34px;border-radius:50%;background:var(--purple);flex:none}
.brand__text{font-family:"Montserrat",sans-serif;font-weight:700;color:var(--purple);line-height:1.05}
.brand__name{font-size:22px}
.brand__sub{font-size:8.5px}

.photo{position:absolute;border-radius:50%;z-index:0}
.photo--team{left:270px;top:-40px;width:430px;height:430px;background:radial-gradient(circle at 50% 45%,#f4f6f8 0%,#dfe6ec 45%,#a9b8c8 75%,#5a78a8 100%)}
.photo--volunteers{left:340px;top:-60px;width:420px;height:400px;background:radial-gradient(circle at 45% 50%,#d9c3a8 0%,#b8926d 45%,#6e8b6a 75%,#3e5560 100%)}

.title-disc{position:absolute;left:-60px;top:160px;width:360px;height:360px;border-radius:50%;background:var(--blue);opacity:.95}
.title{position:absolute;left:60px;top:250px;font-family:"Fjalla One",sans-serif;font-size:40px;line-height:1.02;color:#fff;text-transform:uppercase;width:230px}

.h-green{font-family:"Montserrat",sans-serif;font-weight:600;color:var(--green);line-height:1.15}
.h-blue{font-family:"Montserrat",sans-serif;font-weight:600;color:var(--blue-deep);line-height:1.15}
.body{font-size:13px;line-height:1.35}
.body p+p{margin-top:6px}

.intro{left:50px;top:535px;width:360px}
.intro .h-green{font-size:21px;margin-bottom:10px}
.intro .h-blue{font-size:20px;margin:14px 0 8px}

.panel{position:absolute;left:435px;top:520px;width:345px;height:560px;background:var(--purple);border-top-left-radius:32px;color:#fff;padding:24px 24px 0 26px;z-index:2}
.checks{list-style:none;font-family:"Montserrat",sans-serif;font-weight:500;font-size:13.5px;line-height:1.25}
.checks li{display:flex;gap:9px;margin-bottom:12px}
.checks svg{flex:none;margin-top:2px}
.join{display:flex;align-items:center;justify-content:center;gap:8px;font-size:11px;margin-top:8px;white-space:nowrap}
.join__box{width:26px;height:26px;background:var(--blue-deep);flex:none}
.join--dark{color:var(--ink);margin-top:0}
.pill{display:block;margin:22px auto 0;width:230px;padding:8px 0;border-radius:22px;background:linear-gradient(#3fa33a,var(--green-dark));font-family:"Montserrat",sans-serif;font-weight:700;font-size:18px;text-align:center;color:#fff}

.band{position:absolute;left:0;bottom:0;width:780px;height:270px}
.band--back{height:240px}
.contact{position:absolute;left:60px;bottom:26px;color:#fff;z-index:3}
.contact__title{font-family:"Montserrat",sans-serif;font-weight:600;font-size:28px;margin-bottom:8px}
.contact__row{display:flex;align-items:center;gap:12px;font-size:15px;margin-bottom:7px}
.contact__icon{width:30px;height:30px;border-radius:50%;background:var(--green);display:flex;align-items:center;justify-content:center}

.vision{position:absolute;left:0;top:50px;width:440px;height:290px;z-index:1}
.vision__text{position:absolute;left:36px;top:95px;font-family:"Montserrat",sans-serif;color:#fff;font-weight:600;font-size:19px;line-height:1.22;width:290px;z-index:2}
.vision__text b{display:block;color:var(--green);font-size:30px;margin-bottom:6px}
.col-left{left:50px;top:360px;width:340px}
.col-right{left:420px;top:360px;width:320px}
.col-left .h-green,.col-right .h-green{font-size:22px;margin:0 0 6px}
.col-left section+section{margin-top:18px}
.back-join{right:24px;top:800px}
.back-brand{left:580px;top:880px}
</style>
</head>
<body>

<article class="page page--front">
  <div class="photo photo--team" role="img" aria-label="Photo of a smiling medical team in a hospital corridor"></div>
  <div class="brand abs" style="left:40px;top:40px">
    <span class="brand__dot"></span>
    <span class="brand__text"><span class="brand__name">NKNA</span><br><span class="brand__sub">Nourish Kin Network Australia</span></span>
  </div>
  <div class="title-disc"></div>
  <h1 class="title">Does your child have an eating disorder?</h1>

  <div class="intro abs">
    <h2 class="h-green">Are you concerned your child has a problem with eating, weight or body image?</h2>
    <div class="body">
      <p>Parents and carers play a pivotal role in treatment &amp; recovery of eating disorders.</p>
      <p>NKNA will help you get the skills &amp; knowledge you need to support your loved one through this illness.</p>
    </div>
    <h2 class="h-blue">Welcome to Nourish Kin Network Australia (NKNA)</h2>
    <div class="body"><p>NKNA is an organisation established by a group of Australian parents who have cared for and treated a young person with an eating disorder, to advocate for the needs and roles of other parents during this experience</p></div>
  </div>

  <aside class="panel">
    <ul class="checks">
      <li><svg width="14" height="14" viewBox="0 0 14 14"><circle cx="7" cy="7" r="6" fill="none" stroke="#7ed957" stroke-width="1.6"/><path d="M4 7.2l2 2 4-4" fill="none" stroke="#7ed957" stroke-width="1.6"/></svg>NKNA supports families and carers of people with an eating disorder</li>
      <li><svg width="14" height="14" viewBox="0 0 14 14"><circle cx="7" cy="7" r="6" fill="none" stroke="#7ed957" stroke-width="1.6"/><path d="M4 7.2l2 2 4-4" fill="none" stroke="#7ed957" stroke-width="1.6"/></svg>Early action is imperative</li>
      <li><svg width="14" height="14" viewBox="0 0 14 14"><circle cx="7" cy="7" r="6" fill="none" stroke="#7ed957" stroke-width="1.6"/><path d="M4 7.2l2 2 4-4" fill="none" stroke="#7ed957" stroke-width="1.6"/></svg>NKNA will help guide you to appropriate resources &amp; support</li>
      <li><svg width="14" height="14" viewBox="0 0 14 14"><circle cx="7" cy="7" r="6" fill="none" stroke="#7ed957" stroke-width="1.6"/><path d="M4 7.2l2 2 4-4" fill="none" stroke="#7ed957" stroke-width="1.6"/></svg>NKNA advocates for parents/carers to be actively involved in treatment team</li>
      <li><svg width="14" height="14" viewBox="0 0 14 14"><circle cx="7" cy="7" r="6" fill="none" stroke="#7ed957" stroke-width="1.6"/><path d="M4 7.2l2 2 4-4" fill="none" stroke="#7ed957" stroke-width="1.6"/></svg>NKNA acknowledges the importance of well-being of ALL family members throughout the ED journey</li>
    </ul>
    <div class="join">Please join us today! <span class="join__box"></span> Follow us</div>
    <span class="pill">Donations welcome</span>
  </aside>

  <svg class="band" viewBox="0 0 780 270" aria-hidden="true">
    <path d="M0 90 C220 50 480 35 780 70 L780 270 L0 270 Z" fill="var(--blue)"/>
    <path d="M0 90 C220 50 480 35 780 70" fill="none" stroke="var(--blue-deep)" stroke-width="5"/>
  </svg>
  <div class="contact">
    <div class="contact__title">Contact Us</div>
    <div class="contact__row"><span class="contact__icon"><svg width="16" height="16" viewBox="0 0 16 16"><path d="M4 2l2 3-1.5 1.5a8 8 0 0 0 5 5L11 10l3 2-1.5 2.5C7 14 2 9 1.5 3.5Z" fill="#fff"/></svg></span>+61-4 5550-1234</div>
    <div class="contact__row"><span class="contact__icon"><svg width="16" height="12" viewBox="0 0 16 12"><rect x="1" y="1" width="14" height="10" fill="none" stroke="#fff" stroke-width="1.4"/><path d="M1 1l7 6 7-6" fill="none" stroke="#fff" stroke-width="1.4"/></svg></span>jordan.ellis@nkna.org.au</div>
    <div class="contact__row"><span class="contact__icon"><svg width="16" height="16" viewBox="0 0 16 16" fill="none" stroke="#fff" stroke-width="1.2"><circle cx="8" cy="8" r="6.5"/><ellipse cx="8" cy="8" rx="3" ry="6.5"/><path d="M1.5 8h13M2.5 5h11M2.5 11h11"/></svg></span>www.nkna.org.au</div>
  </div>
</article>

<article class="page page--back">
  <div class="photo photo--volunteers" role="img" aria-label="Photo of smiling volunteers sorting donation boxes together"></div>
  <svg class="vision" viewBox="0 0 440 290" aria-hidden="true">
    <path d="M0 40 L400 0 C390 150 320 260 120 280 L0 284 Z" fill="var(--purple)"/>
  </svg>
  <div class="vision__text"><b>NKNA's Vision:</b>An Australia where Eating Disorders struggle to emerge, thrive or persist.</div>

  <div class="col-left abs body">
    <section>
      <h2 class="h-green">Why NKNA exists</h2>
      <p>Parents and families of children under 18 years &amp; of adults 18 years &amp; over, are vital to treatment and recovery, but not necessarily equipped or supported to be a part of this process.</p>
      <p>It is best practice for all parents and families to be given the option and support to maximise their role in the care team.</p>
    </section>
    <section>
      <h2 class="h-green">NKNA's Role</h2>
      <p>NKNA will be a helpful resource to educate parents &amp; carers on ways to tackle the ED &amp; how to seek appropriate therapy while being included as part of the treatment team.</p>
    </section>
    <section>
      <h2 class="h-green">Objectives</h2>
      <p>To guide parents &amp; carers of a loved one with an eating disorder to appropriate resources &amp; support</p>
      <p>To advocate for parents &amp; carers to be actively involved in the treatment team</p>
      <p>To encourage good health &amp; well-being for ALL family members during what can be an exhausting, frustrating, overwhelming &amp; scary experience</p>
    </section>
  </div>

  <div class="col-right abs body">
    <h2 class="h-green">What is an Eating Disorder? (ED)</h2>
    <p>An ED occurs when one becomes unhealthily preoccupied with eating, food or body shape/weight. Defined by abnormal eating habits that negatively affect a person's physical &amp; mental health.</p>
    <p>EDs are NOT a choice, but serious &amp; often life-threatening biological brain disorders. They have the highest mortality rate of ALL mental illnesses, from suicide or organ failure.</p>
    <p>EDs are linked with both genetic and environmental factors and are often triggered by an external event, such as bullying, pressure from social media, cultural obsession with thinness, etc.</p>
    <p>EDs are 10 times more prevalent in females, but can affect males as well. They are most common in adolescence, but are emerging at younger ages also.</p>
    <p>Someone with an Eating Disorder needs serious &amp; urgent medical treatment as well as help, support &amp; understanding from family &amp; friends.</p>
  </div>

  <div class="join join--dark abs back-join">Please join us today! <span class="join__box"></span> Follow us</div>
  <div class="brand abs back-brand">
    <span class="brand__dot"></span>
    <span class="brand__text"><span class="brand__name">NKNA</span><br><span class="brand__sub">Nourish Kin Network Australia</span></span>
  </div>

  <svg class="band band--back" viewBox="0 0 780 240" aria-hidden="true">
    <path d="M0 30 C200 0 420 0 560 20 C520 100 480 180 460 240 L0 240 Z" fill="var(--blue)"/>
    <path d="M0 30 C200 0 420 0 560 20" fill="none" stroke="var(--blue-deep)" stroke-width="5"/>
  </svg>
  <div class="contact">
    <div class="contact__title">Contact Us</div>
    <div class="contact__row"><span class="contact__icon"><svg width="16" height="16" viewBox="0 0 16 16"><path d="M4 2l2 3-1.5 1.5a8 8 0 0 0 5 5L11 10l3 2-1.5 2.5C7 14 2 9 1.5 3.5Z" fill="#fff"/></svg></span>+61-4 5550-1234</div>
    <div class="contact__row"><span class="contact__icon"><svg width="16" height="12" viewBox="0 0 16 12"><rect x="1" y="1" width="14" height="10" fill="none" stroke="#fff" stroke-width="1.4"/><path d="M1 1l7 6 7-6" fill="none" stroke="#fff" stroke-width="1.4"/></svg></span>jordan.ellis@nkna.org.au</div>
    <div class="contact__row"><span class="contact__icon"><svg width="16" height="16" viewBox="0 0 16 16" fill="none" stroke="#fff" stroke-width="1.2"><circle cx="8" cy="8" r="6.5"/><ellipse cx="8" cy="8" rx="3" ry="6.5"/><path d="M1.5 8h13M2.5 5h11M2.5 11h11"/></svg></span>www.nkna.org.au</div>
  </div>
</article>

</body>
</html>
```